Boutique Salon Brand Refresh needs color palette, font, templates.

Lorvu Hair Design is an established hair salon celebrating 10 years in business. We are currently evolving our brand to better reflect who we are today, the clients we serve, and the direction we want to take our business moving forward.
Our goal is to position Lorvu as a refined, modern boutique salon created specifically for “The Lorvu Woman.”
In the past, much of our branding and marketing focused on us—our salon, our space, our services, and our team. Going forward, we want to shift that focus to her: who she is, what she values, how she wants to look and feel, and how Lorvu fits into her life.
We want our brand to communicate expertise and quality without feeling overly luxurious, trendy, intimidating, or impersonal. It should feel polished, sophisticated, warm, approachable, and timeless—a boutique experience designed for women who value beautiful, healthy hair and trusted professional guidance.
As part of this rebrand, we are looking to establish a cohesive visual identity that can be carried consistently across our website, social media, email marketing, print materials, signage, and other client touchpoints.

*** For THIS PROJECT, we are SPECIFICALLY LOOKING for:
- A cohesive brand color palette
- 2–3 complementary fonts for consistent use across our marketing
- 4–5 customizable social media templates that can be used across Instagram and Facebook
A visual direction that feels distinctive to Lorvu and speaks directly to The Lorvu Woman.
The following information provides more detail about The Lorvu Woman, our positioning, brand personality, values, and the overall direction we envision for the next chapter of Lorvu Hair Design.
Lorvu Hair Design
Alder Falls, NJ USA
lorvuhairstudio.example

--PRIMARY AUDIENCE
The Lorvu woman values quality, consistency, and professional guidance.
She wants to look polished and current without appearing overdone or overly trendy.
She may be managing grey hair, changing texture, thinning, dryness, fading color, or a style that no longer reflects who she is. She wants an expert who understands these concerns and can create a realistic plan.
She is willing to invest in professional services and products when she understands their value.
She does not want to experiment with her appearance.
She wants to feel confident in the person caring for her hair.
Women approximately 45 to 65 years old living in Mendham, Morris County, and surrounding communities.

--COLOR PALETTE
The overall appearance should feel calm, spacious, editorial, and cohesive. The entire visual system should feel more like a refined boutique hotel, skincare brand, or luxury lifestyle publication than a traditional salon advertisement.
When choosing the palette, we want the colors to invoke these feelings.
Represents:
Expertise
Confidence
Timelessness
Professionalism
Calm
Warmth
Cleanliness
Soft luxury
Natural beauty
Warmth
Balance
Subtle sophistication
Consistency

--TYPOGRAPHY
The typography system should feel refined, modern, readable, and timeless.
Recommended usage for each font, size, spacing, etc.

----TEMPLATE IDEAS
**EDUCATIONAL POST
Frequently asked questions
Healthy-hair advice
Healthy Hair Tip
Grey Coverage FAQ
Grey Blending FAQ
Product education
Single-tip graphic
**REVIEWS
Google reviews
Finest in Town recognition/Community awards
Long-term guest relationships
Guest testimonials/satisfaction stories
Referral stories
**ADS
**SALON UPDATES/INFO
Holiday hours
Policy reminder
New guest guide
Consultation invitation
Service spotlight
Seasonal guidance
**ABOUT LORVU
Who we are
What to expect from us
What we can provide
Our expertise
**HIGHLIGHT ICON
Questions
Testimonial
Product
Reminders

TEMPLATE RULES
Use the color palette
Use only the font system
Maintain generous spacing
Limit text
Use consistent margins
Keep calls to action simple
Avoid crowded layouts
Use photography intentionally
Keep every template recognizably Lorvu

Target Market(s)

Women approximately 45 to 65 years old living in Mendham, Morris County, and surrounding communities. She values quality, consistency, and professional guidance. She wants to look polished and current without appearing overdone or overly trendy. She is willing to invest in professional services and products when she understands their value.

Industry/Entity Type

Hair Salon

Font styles to use
Serif
Sans Serif
Script

Requirements
Must have
• We are looking to establish a cohesive visual identity that can be carried consistently across platforms. It should communicate expertise and quality without feeling overly fluffy, trendy, intimidating, or impersonal. I would like to see multiple template ideas. Example- one template for education post, one template for reviews, one for salon information/updates. etc. My main goal here is to simplify social media posts by having designated templates for each post category. WE WILL BE KEEPING OUR ORGINAL LOGO- SO COLOR PALETTE MUST REFLECT THAT.
Nice to have
• Color palette and font sets that reflect the brand. **cohesive visual identity**
Should not have
• Nothing flashy, busy, overly trendy.

```html
<!DOCTYPE html>
<html lang="en">
<head>
<meta charset="utf-8">
<title>The Lorvu Woman — Brand Sheet</title>
<link href="https://fonts.googleapis.com/css2?family=Cormorant+Garamond:wght@500;600&family=Jost:ital,wght@0,400;0,500;0,600;1,600&family=Allura&display=swap" rel="stylesheet">
<style>
  :root {
    --page: #efeeec;
    --ink: #4e4238;
    --gold-text: #c0a25e;
    --gold-line: #dcbf74;
    --band-top: #e4c67d;
    --band-bottom: #dbb462;
    --card-top: #efeeeb;
    --card-bottom: #dcd8cf;
    --button: #bba76f;
    --leaf: #7cc94a;
    --hair-light: #c9864e;
    --hair-dark: #8a4f2b;
  }
  * { margin: 0; padding: 0; box-sizing: border-box; }
  html, body { width: 1200px; height: 1200px; overflow: hidden; background: var(--page); }
  .board { position: relative; width: 1200px; height: 1200px; }

  .brand-header .rule { position: absolute; top: 297px; height: 1.5px; background: var(--ink); }
  .brand-header .rule.left { left: 72px; width: 342px; }
  .brand-header .rule.right { left: 784px; width: 344px; }
  .brand-name {
    position: absolute; left: 414px; width: 370px; top: 266px; text-align: center;
    font-family: "Cormorant Garamond", serif; font-weight: 500; font-size: 48px;
    line-height: 1; color: var(--ink); letter-spacing: 0.5px;
  }

  .post {
    position: absolute; top: 538px; width: 523px; height: 523px; overflow: hidden;
    background: linear-gradient(180deg, var(--card-top), var(--card-bottom));
    font-family: "Jost", sans-serif; color: var(--ink);
  }
  .post.promo { left: 56px; }
  .post.faq { left: 621px; }
  .post .deco { position: absolute; inset: 0; }
  .post-brand {
    position: absolute; width: 187px; left: 336px; text-align: center;
    font-family: "Cormorant Garamond", serif; font-weight: 500; font-size: 30px;
    line-height: 1.05; color: var(--ink);
  }
  .headline {
    position: absolute; left: 46px; font-family: "Cormorant Garamond", serif;
    font-weight: 500; font-size: 40px; line-height: 45px; color: var(--ink); text-transform: uppercase;
  }
  .tagline {
    position: absolute; left: 42px; top: 172px; font-family: "Allura", cursive;
    font-size: 38px; color: var(--gold-text);
  }
  .intro { position: absolute; left: 46px; top: 240px; font-size: 13px; line-height: 18px; }
  .discover {
    position: absolute; left: 46px; top: 293px; font-size: 14px; font-weight: 600;
    line-height: 22px; color: var(--gold-text); text-transform: uppercase;
  }
  .location { position: absolute; left: 46px; top: 364px; font-size: 13px; }
  .cta {
    position: absolute; background: var(--button); color: var(--ink); border-radius: 16px;
    height: 32px; display: flex; align-items: center; justify-content: center;
  }
  .promo .cta { left: 38px; top: 398px; width: 252px; font-size: 15px; letter-spacing: 0.3px; }
  .faq .cta { left: 42px; top: 410px; width: 440px; font-size: 18px; font-weight: 600; font-style: italic; }
  .website {
    position: absolute; left: 46px; top: 466px; font-size: 13px;
    display: flex; align-items: center; gap: 5px;
  }
  .qa { position: absolute; left: 46px; width: 290px; font-size: 12.5px; line-height: 18px; }
  .qa .label { position: absolute; left: 0; font-weight: 600; }
  .qa p { padding-left: 20px; }
  .qa.question { top: 170px; font-weight: 600; }
  .qa.answer { top: 221px; }
</style>
</head>
<body>
<main class="board">

  <header class="brand-header">
    <span class="rule left"></span>
    <h1 class="brand-name">The Lorvu Woman</h1>
    <span class="rule right"></span>
  </header>

  <section class="post promo">
    <svg class="deco" width="523" height="523" viewBox="0 0 523 523">
      <defs>
        <linearGradient id="bandFill" x1="0" y1="0" x2="0" y2="1">
          <stop offset="0" stop-color="var(--band-top)"/><stop offset="1" stop-color="var(--band-bottom)"/>
        </linearGradient>
        <linearGradient id="hairFill" x1="0" y1="0" x2="1" y2="1">
          <stop offset="0" stop-color="var(--hair-dark)"/><stop offset="0.5" stop-color="var(--hair-light)"/><stop offset="1" stop-color="var(--hair-dark)"/>
        </linearGradient>
      </defs>
      <polygon fill="url(#bandFill)" points="339,0 523,0 523,523 350,523 346,470 351,420 344,360 349,300 342,240 347,180 340,120 345,60"/>
      <circle cx="-12" cy="-22" r="100" fill="none" stroke="var(--gold-line)" stroke-width="1.2"/>
      <path role="img" aria-label="Photo: woman seen from behind with long wavy caramel hair" fill="url(#hairFill)" d="M300 523 L285 420 Q270 330 310 250 Q345 165 410 165 Q470 170 490 250 Q520 330 523 400 L523 523 Z"/>
      <circle cx="520" cy="462" r="216" fill="none" stroke="var(--gold-line)" stroke-width="1.4"/>
      <ellipse role="img" aria-label="Soft-focus green leaf" cx="22" cy="28" rx="48" ry="30" fill="var(--leaf)" opacity="0.8"/>
      <ellipse role="img" aria-label="Soft-focus green leaf" cx="510" cy="470" rx="36" ry="58" fill="var(--leaf)" opacity="0.75"/>
    </svg>
    <p class="post-brand" style="top:52px">The Lorvu<br>Woman</p>
    <h2 class="headline" style="top:92px">Your<br>Best Hair,</h2>
    <p class="tagline">Beautifully You.</p>
    <p class="intro">Expert color. Healthy, radiant hair.<br>Personalized to you and your lifestyle.</p>
    <p class="discover">Discover the Lorvu<br>Experience.</p>
    <p class="location">Alder Falls, NJ</p>
    <p class="cta">BOOK YOUR APPOINTMENT</p>
    <p class="website">
      <svg width="15" height="15" viewBox="0 0 16 16" fill="none" stroke="var(--gold-text)" stroke-width="1.2"><circle cx="8" cy="8" r="6.5"/><ellipse cx="8" cy="8" rx="3" ry="6.5"/><path d="M1.5 8h13M2.5 4.8h11M2.5 11.2h11"/></svg>
      lorvuhairstudio.example
    </p>
  </section>

  <section class="post faq">
    <svg class="deco" width="523" height="523" viewBox="0 0 523 523">
      <defs>
        <linearGradient id="bandFill2" x1="0" y1="0" x2="0" y2="1">
          <stop offset="0" stop-color="var(--band-top)"/><stop offset="1" stop-color="var(--band-bottom)"/>
        </linearGradient>
      </defs>
      <polygon fill="url(#bandFill2)" points="337,0 523,0 523,523 333,523 337,460 331,400 336,340 330,280 335,220 331,160 336,100 332,40"/>
      <circle cx="-12" cy="-22" r="100" fill="none" stroke="var(--gold-line)" stroke-width="1.2"/>
      <circle cx="531" cy="502" r="224" fill="none" stroke="var(--gold-line)" stroke-width="1.4"/>
      <ellipse role="img" aria-label="Soft-focus green leaf" cx="22" cy="28" rx="48" ry="30" fill="var(--leaf)" opacity="0.8"/>
      <ellipse role="img" aria-label="Soft-focus green leaf" cx="505" cy="470" rx="34" ry="56" fill="var(--leaf)" opacity="0.75"/>
    </svg>
    <p class="post-brand" style="top:50px">The Lorvu<br>Woman</p>
    <h2 class="headline" style="top:84px">Frequently<br>Asked</h2>
    <div class="qa question"><span class="label">Q:</span><p>How do I know which color service<br>is right for me?</p></div>
    <div class="qa answer"><span class="label">A:</span><p>It starts with a consultation. Our stylists take the time to understand your hair history, lifestyle, maintenance preferences, and desired result before recommending a service. Whether you're looking to refresh your color, add dimension, brighten your hair, or blend your natural gray, we'll help you find an approach that feels realistic and right for you.</p></div>
    <p class="cta">Let’s create a plan for your hair.</p>
    <p class="website">
      <svg width="15" height="15" viewBox="0 0 16 16" fill="none" stroke="var(--gold-text)" stroke-width="1.2"><circle cx="8" cy="8" r="6.5"/><ellipse cx="8" cy="8" rx="3" ry="6.5"/><path d="M1.5 8h13M2.5 4.8h11M2.5 11.2h11"/></svg>
      lorvuhairstudio.example
    </p>
  </section>

</main>
</body>
</html>
```